This is a a hair cutting class for hair stylist

Flyer with dates time place couple of pics with hair styles. Need it web media compatible. Design needs to be for a 2 sided flier. This flier need to stand out but be clean and professional. Mainly use the top info in the word doc for text in the flier.

done done done done done done done done done done done done done done done done done done done

Target Market(s)

Professional stylist and Cosmetology students

Industry/Entity Type

Hair And Beauty

Font styles to use
Sans Serif

Colors
33a6d7

Requirements
Must have
• Clear text and can use for Instagram and Facebook . must be designed to be used on both sides of a flyer 4x6 .
Nice to have
• picture cleanup if flaws are notices.
Should not have
• dark colors

```html
<!DOCTYPE html>
<html lang="en">
<head>
<meta charset="utf-8">
<title>Short Hair Cuts – Shear Perfection Workshop</title>
<link href="https://fonts.googleapis.com/css2?family=Archivo+Black&family=Oswald:wght@500;600;700&family=Raleway:wght@300;400&family=Libre+Baskerville:wght@400;700&display=swap" rel="stylesheet">
<style>
  :root{
    --brand-blue:#33a6d7;
    --sky:#1aa3e0;
    --deep-blue:#0b5f9e;
    --navy:#0d3f63;
    --red:#d91f26;
    --red-dark:#a8141a;
    --ink:#1a1a1a;
    --grey:#7a7a7a;
    --white:#ffffff;
  }
  *{margin:0;padding:0;box-sizing:border-box}
  html,body{width:845px;height:1200px;overflow:hidden;background:#fff}
  .flyer{
    position:relative;width:845px;height:1200px;overflow:hidden;
    background:linear-gradient(180deg,#1697d8 0%,#2fb0e6 30%,#6cc6ee 52%,#cfeaf8 64%,#ffffff 72%);
    font-family:'Oswald',sans-serif;
  }
  .hero-photo{
    position:absolute;left:360px;top:40px;width:485px;height:720px;
    background:radial-gradient(ellipse closest-side at 50% 48%,#0e1d3a 0%,#1b3565 40%,rgba(63,120,184,.85) 70%,rgba(120,180,230,0) 100%);
  }
  .stylist-name{
    position:absolute;left:57px;top:46px;white-space:nowrap;
    font-family:'Archivo Black',sans-serif;font-size:50px;color:var(--white);letter-spacing:-1px;line-height:1;
  }
  .stylist-title{
    position:absolute;left:57px;top:102px;width:240px;height:22px;background:var(--white);
    font-family:'Raleway',sans-serif;font-weight:400;font-size:20px;line-height:22px;color:var(--deep-blue);padding-left:3px;letter-spacing:.5px;white-space:nowrap;
  }
  .headline{
    position:absolute;left:57px;font-weight:600;font-size:68px;line-height:1;letter-spacing:-1px;white-space:nowrap;
  }
  .headline.light{color:#e3f4fc}
  .headline.dark{color:var(--navy);font-weight:700}
  .workshop-box{
    position:absolute;left:62px;top:420px;width:366px;height:96px;background:var(--white);
    border-left:6px solid var(--navy);padding:6px 0 0 10px;white-space:nowrap;
  }
  .workshop-box .big{font-family:'Raleway',sans-serif;font-weight:300;font-size:52px;line-height:1;color:var(--ink)}
  .workshop-box .sub{font-size:22px;font-weight:600;color:var(--ink);line-height:1.3;letter-spacing:-.3px}
  .badge{position:absolute;border-radius:50%;text-align:center;overflow:hidden}
  .date-badge{
    left:59px;top:531px;width:354px;height:354px;
    background:radial-gradient(circle at 45% 35%,#ffffff 55%,#e3f2fb 78%,#9fd3ef 100%);
    border:5px solid var(--brand-blue);box-shadow:0 4px 10px rgba(0,0,0,.25);
    font-family:'Libre Baskerville',serif;
  }
  .date-badge span{position:absolute;white-space:nowrap;line-height:1}
  .date-badge .day{left:70px;top:52px;font-size:26px;color:var(--brand-blue)}
  .date-badge .month{left:28px;top:84px;font-size:62px;font-weight:700;color:var(--navy);letter-spacing:-2px}
  .date-badge .time{left:80px;top:158px;font-size:34px;color:var(--brand-blue)}
  .date-badge .year{left:70px;top:198px;font-size:42px;font-weight:700;color:var(--navy)}
  .date-badge .num{left:200px;top:20px;font-size:230px;font-weight:700;color:var(--deep-blue)}
  .date-badge .venue{
    position:absolute;left:0;right:0;top:244px;bottom:0;
    background:linear-gradient(180deg,#2ea4de,#1480c4);color:var(--white);
    font-family:'Oswald',sans-serif;padding-top:4px;line-height:1.15;
  }
  .venue .salon{font-size:22px;font-weight:600;color:var(--ink)}
  .venue .addr{font-size:18px;font-weight:500}
  .price{
    background:radial-gradient(circle at 45% 30%,#ef3b3f 0%,var(--red) 55%,var(--red-dark) 100%);
    border:4px solid #f3f3f3;box-shadow:0 4px 10px rgba(0,0,0,.3);color:var(--white);
  }
  .price .label{font-weight:500;font-size:22px;line-height:1.1}
  .price .amount{font-weight:600;font-size:58px;line-height:1;letter-spacing:-2px}
  .price .amount sup{font-size:24px;vertical-align:top;letter-spacing:0}
  .price-full{left:415px;top:651px;width:198px;height:198px;padding-top:46px}
  .price-full .label small{font-size:16px}
  .price-obs{left:63px;top:874px;width:194px;height:194px;padding-top:46px}
  .book-badge{
    left:288px;top:843px;width:204px;height:204px;padding-top:42px;
    background:radial-gradient(circle at 45% 35%,#ffffff 60%,#dfeef8 85%,#aacde6 100%);
    border:6px solid var(--navy);box-shadow:0 4px 10px rgba(0,0,0,.3);color:var(--ink);
  }
  .book-badge .top{font-size:19px;font-weight:500}
  .book-badge .book{font-size:64px;font-weight:700;color:var(--sky);line-height:.95;-webkit-text-stroke:1px var(--deep-blue)}
  .book-badge .bottom{font-size:23px;font-weight:500}
  .overview{position:absolute;right:70px;top:860px;text-align:right;line-height:1.12}
  .overview h2{font-family:'Libre Baskerville',serif;font-weight:700;font-size:24px;color:var(--grey);margin-bottom:4px}
  .overview .tier{font-weight:700;font-size:21px;color:var(--red);margin-top:6px}
  .overview .item{font-weight:500;font-size:18px;color:var(--deep-blue);margin-top:6px}
  .contact{position:absolute;left:58px;top:1075px;white-space:nowrap}
  .contact .lead{font-family:'Raleway',sans-serif;font-weight:300;font-size:31px;color:var(--ink)}
  .contact .phones{font-weight:700;font-size:42px;color:var(--sky);letter-spacing:.5px;line-height:1.2}
  .contact .phones .or{font-size:25px;color:var(--navy)}
</style>
</head>
<body>
<main class="flyer">
  <div class="hero-photo" role="img" aria-label="Photo of a client with a curly short haircut, seen from behind"></div>

  <div class="stylist-name">DANA MOREL</div>
  <div class="stylist-title">MASTER STYLIST</div>

  <h1>
    <span class="headline light" style="top:134px">SHORT</span>
    <span class="headline light" style="top:204px">HAIR CUTS</span>
    <span class="headline dark" style="top:276px">SHEAR</span>
    <span class="headline dark" style="top:346px">PERFECTION</span>
  </h1>

  <div class="workshop-box">
    <div class="big">Hands on</div>
    <div class="sub">SHORT HAIRCUTTING WORKSHOP</div>
  </div>

  <div class="badge date-badge">
    <span class="num">2</span>
    <span class="day">SUNDAY</span>
    <span class="month">APRIL</span>
    <span class="time">9-5PM</span>
    <span class="year">2017</span>
    <div class="venue">
      <div class="salon">THE LILA FERN SALON</div>
      <div class="addr">418 NE ALDER ROW, FAIRVIEW<br>OREGON 97000</div>
    </div>
  </div>

  <div class="badge price price-full">
    <div class="label">OBSERVATION<br><small>AND</small> HANDS ON</div>
    <div class="amount"><sup>$</sup>275<sup>.00</sup></div>
  </div>

  <div class="badge price price-obs">
    <div class="label">OBSERVATION<br>ONLY</div>
    <div class="amount"><sup>$</sup>175<sup>.00</sup></div>
  </div>

  <div class="badge book-badge">
    <div class="top">LIMITED OFFER!</div>
    <div class="book">BOOK</div>
    <div class="bottom">YOURS TODAY</div>
  </div>

  <section class="overview">
    <h2>Class Overview</h2>
    <div class="tier">Observation Only</div>
    <div class="item">HAIR CONSULTATION</div>
    <div class="item">STEP-BY-STEP HAIRCUTTING<br>DEMONSTRATION</div>
    <div class="tier">Hands-on Haircutting</div>
    <div class="item">PRACTICE SHORT<br>HAIRCUTTING</div>
  </section>

  <div class="contact">
    <div class="lead">Booking &amp; Inquiries, please call</div>
    <div class="phones">555 204 7731 <span class="or">OR</span> 555 619 4082</div>
  </div>
</main>
</body>
</html>
```